Sleep Consulting Business

Hello I need a business card design with similar colors to my logo that was created. I help mom/parents whose little ones are having sleep issues. Are you able to recreate the picture with the girl sleeping onto a business card using a picture that I provide. That would be one side with my logo on top and on the other side would the following:
My name (in bigger letters than the rest. maybe written in script
title
email
website
phone
instagram
I have included color Inspo
Contact Information for Business Card
Full Name, number, email, website, ig page
Look and feel
Each slider illustrates characteristics of the customer's brand and the style your logo design should communicate.

```html
<!DOCTYPE html>
<html lang="en">
<head>
<meta charset="utf-8">
<title>Nestled Nights – Business Card</title>
<link href="https://fonts.googleapis.com/css2?family=Dancing+Script:wght@600&family=Montserrat:wght@400;600&display=swap" rel="stylesheet">
<style>
  :root{
    --stage:#a9a9ab;
    --terracotta:#c8917a;
    --terracotta-deep:#b97c66;
    --paper:#fbfaf8;
    --ink:#1d1d1d;
    --muted:#7b7472;
    --icon:#8a8583;
    --glow:#f1e6df;
  }
  *{box-sizing:border-box;margin:0;padding:0}
  html,body{width:1200px;height:768px;overflow:hidden}
  body{
    background:var(--stage);
    display:flex;align-items:center;justify-content:center;gap:40px;
    font-family:"Montserrat",Arial,sans-serif;
  }
  .card{
    width:540px;height:312px;border-radius:22px;position:relative;overflow:hidden;
    box-shadow:0 10px 24px rgba(0,0,0,.18);
  }
  /* back side */
  .card--back{
    background:var(--terracotta);
    display:flex;flex-direction:column;align-items:center;justify-content:center;gap:34px;
    color:#fff;
  }
  .brand-mark{display:flex;align-items:center;gap:14px}
  .brand-mark__dot{width:18px;height:18px;border-radius:50%;background:#fff}
  .brand-name{font-family:"Montserrat",Arial,sans-serif;font-weight:600;font-size:40px;letter-spacing:1px}
  .card--back .web{font-size:15px;font-weight:600;letter-spacing:4px}
  /* front side */
  .card--front{background:var(--paper)}
  .card--front .brand-mark{position:absolute;left:30px;top:30px}
  .card--front .brand-name{color:var(--terracotta);font-size:26px}
  .card--front .brand-mark__dot{background:var(--terracotta);width:12px;height:12px}
  .decor{
    position:absolute;left:60px;top:110px;width:440px;height:190px;
    background:radial-gradient(ellipse at 72% 55%,var(--glow) 0%,rgba(241,230,223,.5) 45%,rgba(251,250,248,0) 72%);
  }
  .contact{position:absolute;right:34px;top:120px;width:250px;color:var(--ink)}
  .contact__name{font-family:"Dancing Script",cursive;color:var(--terracotta-deep);font-size:28px;line-height:1}
  .contact__title{color:var(--muted);font-size:12px;margin:2px 0 12px}
  .contact__address{font-size:13px;line-height:1.35;margin-bottom:10px}
  .contact__list{list-style:none;font-size:13px;line-height:1.5}
  .contact__list li{display:flex;align-items:center;gap:8px}
  .contact__list svg{width:13px;height:13px;flex:none}
</style>
</head>
<body>
  <section class="card card--back" aria-label="Card back">
    <div class="brand-mark"><span class="brand-mark__dot"></span><span class="brand-name">Nestled Nights</span></div>
    <p class="web">www.NestledNights.com</p>
  </section>

  <section class="card card--front" aria-label="Card front">
    <div class="brand-mark"><span class="brand-mark__dot"></span><span class="brand-name">Nestled Nights</span></div>
    <div class="decor" role="img" aria-label="Faint brand decoration of a rising sun over soft hills"></div>
    <div class="contact">
      <p class="contact__name">Dana Whitfield</p>
      <p class="contact__title">Chief of Staff</p>
      <p class="contact__address">215 Elm Row, Suite 300<br>Riverton, NC 28400</p>
      <ul class="contact__list">
        <li><svg viewBox="0 0 16 16"><path fill="var(--icon)" d="M3 1l3 3-1.5 2a9 9 0 0 0 5.5 5.5L12 10l3 3-2 2C7 15 1 9 1 3z"/></svg>(555)201-4837</li>
        <li><svg viewBox="0 0 16 16"><rect x="1" y="3" width="14" height="10" rx="1" fill="var(--icon)"/><path d="M1.5 4l6.5 5 6.5-5" stroke="#fff" stroke-width="1.3" fill="none"/></svg>Dana@NestledNights.com</li>
        <li><svg viewBox="0 0 16 16"><circle cx="8" cy="8" r="6.5" fill="none" stroke="var(--icon)" stroke-width="1.5"/><path d="M1.5 8h13M8 1.5c-3 3.5-3 9.5 0 13M8 1.5c3 3.5 3 9.5 0 13" stroke="var(--icon)" stroke-width="1.1" fill="none"/></svg>www.NestledNights.com</li>
        <li><svg viewBox="0 0 16 16"><circle cx="8" cy="8" r="7" fill="var(--icon)"/></svg>@NestledNights</li>
      </ul>
    </div>
  </section>
</body>
</html>
```